Business Card and Stationary for Construction Company
RT Hollis Construction
Professional
Marcus Hollis
General Contractor
Serving the Central Coast
rthollis.build@examplemail.net
License #417862

```html
<!DOCTYPE html>
<html lang="en">
<head>
<meta charset="utf-8">
<title>RT Hollis Construction — Business Card</title>
<link href="https://fonts.googleapis.com/css2?family=Cinzel:wght@400;600&display=swap" rel="stylesheet">
<style>
  :root {
    --page: #ecebe8;
    --card: #ffffff;
    --brand-red: #c8171e;
    --ink: #4a4a4a;
    --rule: #b9b9b9;
  }
  * { margin: 0; padding: 0; box-sizing: border-box; }
  html, body { width: 1200px; height: 914px; overflow: hidden; }
  body {
    background: var(--page);
    display: flex; align-items: center; justify-content: center;
    font-family: "Cinzel", "Times New Roman", serif;
  }
  .business-card {
    width: 1000px; height: 572px;
    background: var(--brand-red);
    padding: 26px;
  }
  .card-face {
    width: 100%; height: 100%;
    background: var(--card);
    display: flex; align-items: center;
    padding: 0 60px 0 70px;
  }
  .brand {
    flex: 0 0 400px;
    display: flex; align-items: center; gap: 14px;
    color: var(--brand-red);
    font-weight: 600;
  }
  .brand-square { width: 18px; height: 18px; background: var(--brand-red); flex: none; }
  .brand-name { font-size: 34px; line-height: 1.1; letter-spacing: 1px; }
  .divider { width: 1px; height: 130px; background: var(--rule); margin: 0 28px 0 40px; align-self: center; transform: translateY(-20px); }
  .contact { color: var(--ink); }
  .person-name { color: var(--brand-red); font-size: 22px; letter-spacing: 0.5px; }
  .person-title { font-size: 17px; margin-bottom: 22px; }
  .contact-list { list-style: none; }
  .contact-list li { display: flex; align-items: center; gap: 10px; font-size: 15px; line-height: 1.75; }
  .contact-icon { width: 16px; height: 16px; flex: none; }
</style>
</head>
<body>
  <div class="business-card">
    <div class="card-face">
      <div class="brand">
        <span class="brand-square"></span>
        <span class="brand-name">RT Hollis Construction</span>
      </div>
      <div class="divider"></div>
      <div class="contact">
        <p class="person-name">Marcus Hollis</p>
        <p class="person-title">General Contractor</p>
        <ul class="contact-list">
          <li>
            <svg class="contact-icon" viewBox="0 0 16 16"><circle cx="8" cy="8" r="8" fill="#c8171e"/><path d="M8 3.5a2.8 2.8 0 0 0-2.8 2.8C5.2 8.5 8 12.5 8 12.5s2.8-4 2.8-6.2A2.8 2.8 0 0 0 8 3.5z" fill="#fff"/><circle cx="8" cy="6.3" r="1" fill="#c8171e"/></svg>
            Serving the Central Coast
          </li>
          <li>
            <svg class="contact-icon" viewBox="0 0 16 16"><circle cx="8" cy="8" r="8" fill="#c8171e"/><path d="M5.2 4.2l1.6-.3.8 2-1 .8a5.5 5.5 0 0 0 2.7 2.7l.8-1 2 .8-.3 1.6c-3.8.3-6.9-2.8-6.6-6.6z" fill="#fff"/></svg>
            (805) 555-0142
          </li>
          <li>
            <svg class="contact-icon" viewBox="0 0 16 16"><circle cx="8" cy="8" r="8" fill="#c8171e"/><path d="M4.6 8.2l2.2 2.2 4.6-4.6" stroke="#fff" stroke-width="1.6" fill="none"/></svg>
            License #417862
          </li>
          <li>
            <svg class="contact-icon" viewBox="0 0 16 16"><circle cx="8" cy="8" r="8" fill="#c8171e"/><rect x="4" y="5" width="8" height="6" fill="#fff"/><path d="M4 5l4 3.4L12 5" stroke="#c8171e" stroke-width="0.9" fill="none"/></svg>
            rthollis.build@examplemail.net
          </li>
        </ul>
      </div>
    </div>
  </div>
</body>
</html>
```